Breakfast Briefings / Lunch & Learn

I would like to have a double sided flyer size 8x10 to display the breakfast briefing on one side and Lunch & Learn on the other side.

Header on each side to say
2018 Calendar Breakfast Briefing (on the breakfast side)
2018 Calendar Lunch & Learn (on the lunch side)

I have attached a copy of the files we would like to use.

Learn

```html
<!DOCTYPE html>
<html lang="en">
<head>
<meta charset="utf-8">
<title>Breakfast Briefings – 2018 Calendar</title>
<link href="https://fonts.googleapis.com/css2?family=Audiowide&family=Arimo:wght@400;700&display=swap" rel="stylesheet">
<style>
  :root {
    --orange: #e8761c;
    --white: #ffffff;
    --ink: #1e2a36;
    --cal-ink: #2a1606;
    --medical: #f6c400;
    --sales: #efe80a;
    --finance: #cbe40c;
    --rnd: #a4dc14;
    --operations: #55d145;
    --clinical: #2fd05e;
    --quality: #30d487;
    --people: #39d6aa;
    --marketing: #3bcdc0;
    --legal: #3cbdd2;
    --access: #3a94d2;
    --tos: #3a6cc6;
    --photo-a: #d9c6a8;
    --photo-b: #8a7258;
  }
  * { box-sizing: border-box; margin: 0; padding: 0; }
  html, body { width: 1008px; height: 1200px; overflow: hidden; background: var(--white); }
  .flyer { position: relative; width: 1008px; height: 1200px; background: var(--white); overflow: hidden; }

  .title-band {
    position: absolute; left: 0; top: 0; width: 100%; height: 52px;
    background: var(--orange);
    display: flex; align-items: center; justify-content: center;
  }
  .title-band h1 {
    font-family: "Audiowide", sans-serif; font-weight: 400;
    color: var(--white); font-size: 36px; letter-spacing: 2px; line-height: 1;
  }

  .cycle-arrows { position: absolute; left: 0; top: 0; width: 1008px; height: 760px; }

  .photo-slot {
    position: absolute; left: 307px; top: 290px; width: 332px; height: 262px;
    background: linear-gradient(135deg, var(--photo-a), var(--photo-b));
  }

  .dept {
    position: absolute; width: 112px; height: 112px; margin: -56px 0 0 -56px;
    border-radius: 50%;
    display: flex; flex-direction: column; align-items: center; justify-content: center;
    text-align: center;
    font-family: "Arimo", sans-serif; color: var(--ink);
    font-size: 13px; line-height: 1.2;
  }
  .dept .name { margin-top: 3px; }
  .dept .when { font-weight: 700; margin-top: 3px; }
  .dept--light { color: var(--white); }

  .calendar {
    position: absolute; left: 0; top: 757px; width: 100%; height: 443px;
    background: var(--orange);
  }
  .calendar .year {
    position: absolute; right: 14px; top: 6px;
    font-family: "Audiowide", sans-serif; color: var(--white); font-size: 44px;
  }
  .months {
    position: absolute; left: 17px; top: 44px;
    display: grid; grid-template-columns: repeat(4, 254px); grid-auto-rows: 137px;
  }
  .month { font-family: "Audiowide", sans-serif; color: var(--cal-ink); }
  .month h2 { font-size: 19px; font-weight: 400; line-height: 22px; }
  .weekdays, .days {
    display: grid; grid-template-columns: repeat(7, 30px);
    font-size: 11.5px; line-height: 14.5px;
  }
  .weekdays { font-weight: 700; }
  .days span:first-child { grid-column-start: var(--start); }
</style>
</head>
<body>
<main class="flyer">
  <header class="title-band"><h1>Breakfast Briefings</h1></header>

  <svg class="cycle-arrows" viewBox="0 0 1008 760" aria-hidden="true">
    <defs>
      <polygon id="flow-arrow" points="-12,-5 2,-5 2,-11 12,0 2,11 2,5 -12,5"/>
    </defs>
    <use href="#flow-arrow" fill="#f6c400" transform="translate(595 145) rotate(23)"/>
    <use href="#flow-arrow" fill="#efe80a" transform="translate(719 230) rotate(50)"/>
    <use href="#flow-arrow" fill="#cbe40c" transform="translate(785 345) rotate(70)"/>
    <use href="#flow-arrow" fill="#a4dc14" transform="translate(785 480) rotate(108)"/>
    <use href="#flow-arrow" fill="#55d145" transform="translate(718 602) rotate(130)"/>
    <use href="#flow-arrow" fill="#2fd05e" transform="translate(594 674) rotate(166)"/>
    <use href="#flow-arrow" fill="#30d487" transform="translate(439 674) rotate(195)"/>
    <use href="#flow-arrow" fill="#39d6aa" transform="translate(318 603) rotate(228)"/>
    <use href="#flow-arrow" fill="#3bcdc0" transform="translate(245 486) rotate(247)"/>
    <use href="#flow-arrow" fill="#3cbdd2" transform="translate(245 351) rotate(292)"/>
    <use href="#flow-arrow" fill="#3a94d2" transform="translate(318 232) rotate(312)"/>
    <use href="#flow-arrow" fill="#3a6cc6" transform="translate(439 147) rotate(335)"/>
  </svg>

  <div class="photo-slot" role="img" aria-label="Breakfast table with a tablet showing the 2018 Calendar Breakfast Briefings title, coffee, orange juice and croissants"></div>

  <section class="schedule">
    <div class="dept" style="left:515px;top:112px;background:var(--medical)"><span>Medical</span><span class="name">Dana<br>Carlow</span><span class="when">2019<br>TBD</span></div>
    <div class="dept" style="left:676px;top:179px;background:var(--sales)"><span>Sales</span><span class="name">Jon Avery</span><span class="when">2019<br>TBD</span></div>
    <div class="dept" style="left:762px;top:281px;background:var(--finance)"><span>Finance</span><span class="name">Ray Colton</span><span class="when">March</span></div>
    <div class="dept" style="left:808px;top:410px;background:var(--rnd)"><span>R&amp;D</span><span class="name">Chris<br>Castellan</span><span class="when">April</span></div>
    <div class="dept" style="left:762px;top:550px;background:var(--operations)"><span>Operations</span><span class="name">Peter<br>Hollis</span><span class="when">May</span></div>
    <div class="dept" style="left:674px;top:654px;background:var(--clinical)"><span>Clinical/ Reg</span><span class="name">Ben Garner</span><span class="when">June</span></div>
    <div class="dept" style="left:515px;top:695px;background:var(--quality)"><span>Quality</span><span class="name">Derek<br>Ashford</span><span class="when">July</span></div>
    <div class="dept" style="left:363px;top:654px;background:var(--people)"><span>People</span><span class="name">Dina<br>Ghosal</span><span class="when">August</span></div>
    <div class="dept" style="left:273px;top:553px;background:var(--marketing)"><span>Marketing</span><span class="name">Nikhil<br>Tandon</span><span class="when">September</span></div>
    <div class="dept" style="left:217px;top:419px;background:var(--legal)"><span>Legal</span><span class="name">Karim<br>Rahman</span><span class="when">October</span></div>
    <div class="dept" style="left:273px;top:283px;background:var(--access)"><span>Market<br>Access</span><span class="name">Kathleen<br>Northrup</span><span class="when">November</span></div>
    <div class="dept dept--light" style="left:363px;top:182px;background:var(--tos)"><span>TOS</span><span class="name">Clara Stone</span><span class="when">December</span></div>
  </section>

  <section class="calendar">
    <div class="year">2018</div>
    <div class="months">
      <div class="month"><h2>January</h2><div class="weekdays"><span>M</span><span>T</span><span>W</span><span>T</span><span>F</span><span>S</span><span>S</span></div>
        <div class="days" style="--start:1"><span>1</span><span>2</span><span>3</span><span>4</span><span>5</span><span>6</span><span>7</span><span>8</span><span>9</span><span>10</span><span>11</span><span>12</span><span>13</span><span>14</span><span>15</span><span>16</span><span>17</span><span>18</span><span>19</span><span>20</span><span>21</span><span>22</span><span>23</span><span>24</span><span>25</span><span>26</span><span>27</span><span>28</span><span>29</span><span>30</span><span>31</span></div></div>
      <div class="month"><h2>February</h2><div class="weekdays"><span>M</span><span>T</span><span>W</span><span>T</span><span>F</span><span>S</span><span>S</span></div>
        <div class="days" style="--start:4"><span>1</span><span>2</span><span>3</span><span>4</span><span>5</span><span>6</span><span>7</span><span>8</span><span>9</span><span>10</span><span>11</span><span>12</span><span>13</span><span>14</span><span>15</span><span>16</span><span>17</span><span>18</span><span>19</span><span>20</span><span>21</span><span>22</span><span>23</span><span>24</span><span>25</span><span>26</span><span>27</span><span>28</span></div></div>
      <div class="month"><h2>March</h2><div class="weekdays"><span>M</span><span>T</span><span>W</span><span>T</span><span>F</span><span>S</span><span>S</span></div>
        <div class="days" style="--start:4"><span>1</span><span>2</span><span>3</span><span>4</span><span>5</span><span>6</span><span>7</span><span>8</span><span>9</span><span>10</span><span>11</span><span>12</span><span>13</span><span>14</span><span>15</span><span>16</span><span>17</span><span>18</span><span>19</span><span>20</span><span>21</span><span>22</span><span>23</span><span>24</span><span>25</span><span>26</span><span>27</span><span>28</span><span>29</span><span>30</span><span>31</span></div></div>
      <div class="month"><h2>April</h2><div class="weekdays"><span>M</span><span>T</span><span>W</span><span>T</span><span>F</span><span>S</span><span>S</span></div>
        <div class="days" style="--start:7"><span>1</span><span>2</span><span>3</span><span>4</span><span>5</span><span>6</span><span>7</span><span>8</span><span>9</span><span>10</span><span>11</span><span>12</span><span>13</span><span>14</span><span>15</span><span>16</span><span>17</span><span>18</span><span>19</span><span>20</span><span>21</span><span>22</span><span>23</span><span>24</span><span>25</span><span>26</span><span>27</span><span>28</span><span>29</span><span>30</span></div></div>
      <div class="month"><h2>May</h2><div class="weekdays"><span>M</span><span>T</span><span>W</span><span>T</span><span>F</span><span>S</span><span>S</span></div>
        <div class="days" style="--start:2"><span>1</span><span>2</span><span>3</span><span>4</span><span>5</span><span>6</span><span>7</span><span>8</span><span>9</span><span>10</span><span>11</span><span>12</span><span>13</span><span>14</span><span>15</span><span>16</span><span>17</span><span>18</span><span>19</span><span>20</span><span>21</span><span>22</span><span>23</span><span>24</span><span>25</span><span>26</span><span>27</span><span>28</span><span>29</span><span>30</span><span>31</span></div></div>
      <div class="month"><h2>June</h2><div class="weekdays"><span>M</span><span>T</span><span>W</span><span>T</span><span>F</span><span>S</span><span>S</span></div>
        <div class="days" style="--start:5"><span>1</span><span>2</span><span>3</span><span>4</span><span>5</span><span>6</span><span>7</span><span>8</span><span>9</span><span>10</span><span>11</span><span>12</span><span>13</span><span>14</span><span>15</span><span>16</span><span>17</span><span>18</span><span>19</span><span>20</span><span>21</span><span>22</span><span>23</span><span>24</span><span>25</span><span>26</span><span>27</span><span>28</span><span>29</span><span>30</span></div></div>
      <div class="month"><h2>July</h2><div class="weekdays"><span>M</span><span>T</span><span>W</span><span>T</span><span>F</span><span>S</span><span>S</span></div>
        <div class="days" style="--start:7"><span>1</span><span>2</span><span>3</span><span>4</span><span>5</span><span>6</span><span>7</span><span>8</span><span>9</span><span>10</span><span>11</span><span>12</span><span>13</span><span>14</span><span>15</span><span>16</span><span>17</span><span>18</span><span>19</span><span>20</span><span>21</span><span>22</span><span>23</span><span>24</span><span>25</span><span>26</span><span>27</span><span>28</span><span>29</span><span>30</span><span>31</span></div></div>
      <div class="month"><h2>August</h2><div class="weekdays"><span>M</span><span>T</span><span>W</span><span>T</span><span>F</span><span>S</span><span>S</span></div>
        <div class="days" style="--start:3"><span>1</span><span>2</span><span>3</span><span>4</span><span>5</span><span>6</span><span>7</span><span>8</span><span>9</span><span>10</span><span>11</span><span>12</span><span>13</span><span>14</span><span>15</span><span>16</span><span>17</span><span>18</span><span>19</span><span>20</span><span>21</span><span>22</span><span>23</span><span>24</span><span>25</span><span>26</span><span>27</span><span>28</span><span>29</span><span>30</span><span>31</span></div></div>
      <div class="month"><h2>September</h2><div class="weekdays"><span>M</span><span>T</span><span>W</span><span>T</span><span>F</span><span>S</span><span>S</span></div>
        <div class="days" style="--start:6"><span>1</span><span>2</span><span>3</span><span>4</span><span>5</span><span>6</span><span>7</span><span>8</span><span>9</span><span>10</span><span>11</span><span>12</span><span>13</span><span>14</span><span>15</span><span>16</span><span>17</span><span>18</span><span>19</span><span>20</span><span>21</span><span>22</span><span>23</span><span>24</span><span>25</span><span>26</span><span>27</span><span>28</span><span>29</span><span>30</span></div></div>
      <div class="month"><h2>October</h2><div class="weekdays"><span>M</span><span>T</span><span>W</span><span>T</span><span>F</span><span>S</span><span>S</span></div>
        <div class="days" style="--start:1"><span>1</span><span>2</span><span>3</span><span>4</span><span>5</span><span>6</span><span>7</span><span>8</span><span>9</span><span>10</span><span>11</span><span>12</span><span>13</span><span>14</span><span>15</span><span>16</span><span>17</span><span>18</span><span>19</span><span>20</span><span>21</span><span>22</span><span>23</span><span>24</span><span>25</span><span>26</span><span>27</span><span>28</span><span>29</span><span>30</span><span>31</span></div></div>
      <div class="month"><h2>November</h2><div class="weekdays"><span>M</span><span>T</span><span>W</span><span>T</span><span>F</span><span>S</span><span>S</span></div>
        <div class="days" style="--start:4"><span>1</span><span>2</span><span>3</span><span>4</span><span>5</span><span>6</span><span>7</span><span>8</span><span>9</span><span>10</span><span>11</span><span>12</span><span>13</span><span>14</span><span>15</span><span>16</span><span>17</span><span>18</span><span>19</span><span>20</span><span>21</span><span>22</span><span>23</span><span>24</span><span>25</span><span>26</span><span>27</span><span>28</span><span>29</span><span>30</span></div></div>
      <div class="month"><h2>December</h2><div class="weekdays"><span>M</span><span>T</span><span>W</span><span>T</span><span>F</span><span>S</span><span>S</span></div>
        <div class="days" style="--start:6"><span>1</span><span>2</span><span>3</span><span>4</span><span>5</span><span>6</span><span>7</span><span>8</span><span>9</span><span>10</span><span>11</span><span>12</span><span>13</span><span>14</span><span>15</span><span>16</span><span>17</span><span>18</span><span>19</span><span>20</span><span>21</span><span>22</span><span>23</span><span>24</span><span>25</span><span>26</span><span>27</span><span>28</span><span>29</span><span>30</span><span>31</span></div></div>
    </div>
  </section>
</main>
</body>
</html>
```